GLA

Please send us some options for letterhead I attached our Logo. In addition to the Logo we need this information somewhere on the page

48 Harlow Lane
Millbrook, NY 06417
555-274-9160

```html
<!DOCTYPE html>
<html lang="en">
<head>
<meta charset="utf-8">
<title>GLA Letterhead</title>
<link href="https://fonts.googleapis.com/css2?family=Arimo:wght@400;700&display=swap" rel="stylesheet">
<style>
  :root {
    --brand-brown: #4b3d3b;
    --brand-blue: #1a84cc;
    --ink: #3a3a3a;
    --paper: #ffffff;
  }
  html, body {
    margin: 0;
    padding: 0;
    overflow: hidden;
    background: var(--paper);
  }
  .letterhead {
    position: relative;
    width: 981px;
    height: 1200px;
    background: var(--paper);
    font-family: "Arimo", Arial, sans-serif;
    overflow: hidden;
  }
  .edge-bar {
    position: absolute;
    left: 0;
    width: 100%;
    height: 12px;
    display: flex;
  }
  .edge-bar--top { top: 0; }
  .edge-bar--bottom { bottom: 0; }
  .edge-bar span { display: block; height: 100%; }
  .edge-bar .brown { background: var(--brand-brown); }
  .edge-bar .blue { background: var(--brand-blue); }
  .edge-bar--top .brown { width: 44%; }
  .edge-bar--top .blue { flex: 1; }
  .edge-bar--bottom .blue { width: 56%; }
  .edge-bar--bottom .brown { flex: 1; }

  .brand {
    position: absolute;
    left: 46px;
    top: 48px;
    height: 112px;
    display: flex;
    align-items: center;
    gap: 22px;
  }
  .brand-mark {
    width: 112px;
    height: 112px;
    background: var(--brand-brown);
  }
  .brand-name {
    font-weight: 700;
    font-size: 80px;
    line-height: 1;
    letter-spacing: 3px;
    color: var(--brand-brown);
  }

  .contact {
    position: absolute;
    left: 753px;
    top: 62px;
    color: var(--ink);
    font-weight: 700;
    font-size: 19px;
    line-height: 1.2;
  }
  .contact-phone {
    display: flex;
    align-items: center;
    gap: 6px;
    margin-bottom: 12px;
  }
  .contact-phone svg { width: 17px; height: 17px; }
  .contact-address { margin: 0; font-style: normal; }
</style>
</head>
<body>
  <main class="letterhead">
    <div class="edge-bar edge-bar--top"><span class="brown"></span><span class="blue"></span></div>

    <header class="brand">
      <span class="brand-mark" aria-hidden="true"></span>
      <span class="brand-name">GLA</span>
    </header>

    <section class="contact">
      <div class="contact-phone">
        <svg viewBox="0 0 20 20" aria-hidden="true">
          <circle cx="10" cy="10" r="8.5" fill="none" stroke="var(--brand-blue)" stroke-width="1.6"/>
          <path d="M7 5.5c.6-.4 1.2-.3 1.5.3l.8 1.6c.2.5 0 1-.4 1.3l-.5.4c.5 1.2 1.3 2 2.5 2.6l.4-.5c.3-.4.8-.5 1.3-.3l1.6.8c.6.3.7 .9.3 1.5-.7 1-1.8 1.3-3 .8-2.3-.9-4-2.6-4.9-4.9-.5-1.2-.2-2.3.4-3.1z" fill="var(--brand-blue)"/>
        </svg>
        <span>555-274-9160</span>
      </div>
      <address class="contact-address">
        48 Harlow Lane<br>
        Millbrook, NY 06417
      </address>
    </section>

    <div class="edge-bar edge-bar--bottom"><span class="blue"></span><span class="brown"></span></div>
  </main>
</body>
</html>
```